Brightline Villas Estepona listings flyer

Brightline Villas Estepona are a specialist estate agency focussed solely on selling modern and contemporary homes.

We need an A4 folded flyer to be designed so that Brightline Villas Estepona can leaflet drop all of the modern homes for sale in our area to generate new instructions / listings. We need to engage with owners of those types of homes by posting this marketing material through their letter boxes in the hope that they see our funky and modern design and decide to call us about our services to sell their home, if for sale.

We would like to see sharp lines and a modern design (see our logo for style and colour scheme), with lots of white spaces and using photos which can blend in to the background to provide a powerful and impacting image to set us aside from any other direct mail leaflets which may be in their post box. It needs to show

* Quality
* Style
* Modern and forward thinking in design and outlook
* Professionalism

Front page
Top:
Logo of Brightline Villas Estepona.
Helping you sell your modern home. It’s all we do!

4 property photos in a grid position

Bottom banner
If you are thinking of selling, read on…

INSIDE LEFT & RIGHT (DOUBLE PAGE POSSIBLY BLANK WHITE BACKGROUND)
Title: Use Brightline Villas Estepona – the specialist modern homes agency to sell your home

We bring an exciting and dynamic mix of modern marketing with good old fashioned service to guarantee only the most qualified clients will be viewing your home (use online marketing image)

Marketing packages include stylish online brochures, professional photography, stunning drone video footage, informative video walk thru’s and unique floor plans (use drone and floor plan images)

Targeted social media campaigns focusing on international clientele actively looking to buy property in southern Spain (use social media image)

Bespoke, powerful advertising packages enable worldwide exposure for both online and traditional channels to market. We can be as discreet or as visible as you want us to be to sell your home

During our 20 years on the Costa del Sol, we have built up an enviable network of collaborating agents meaning you only have to instruct one expert real estate agent, Brightline Villas Estepona, to gain maximum exposure for your home

BACK PAGE

If you want service that matches the value of your home, contact us today for a private, personalised consultation. Brightline Villas Estepona. It’s all we do.

Suite 14
Torrenova Office Park
Calle Los Almendros
Valdemoro, Marbella

Tel: +34 952 418 306
Mobil y Whatsapp: +34 677 342 815
Email: info@brightlinevillasestepona.example
www.brightlinevillasestepona.example

Target Market(s)

Wealthy property owners of contemporary and modern homes who are looking to sell their home

Industry/Entity Type

Real Estate Agent

Font styles to use
Serif
Sans Serif

Colors
606060
e7e7e7
f5f5f5

Requirements
Must have
• Classy, professional, modern design with the ability to stand out from other leaflet drops / direct mail in letter box
Nice to have
• straight lines to border photos
• Maybe extend the lines further than they should so it has the look of an architects plan
• Blend in images to white background in the middle open double page
Should not have
• Lots of different colours

```html
<!DOCTYPE html>
<html lang="en">
<head>
<meta charset="utf-8">
<title>Brightline Villas Estepona – Folded Flyer</title>
<link rel="stylesheet" href="https://fonts.googleapis.com/css2?family=Oswald:wght@300;400;600&family=Open+Sans:ital,wght@0,400;0,600;1,400&display=swap">
<style>
  :root {
    --ink: #606060;
    --ink-dark: #4a4a4a;
    --line: #6a6a6a;
    --paper: #ffffff;
    --paper-soft: #f5f5f5;
    --paper-mid: #e7e7e7;
    --stage: #cfcfd3;
    --banner: rgba(30, 30, 30, 0.82);
    --sky: #7cc4f4;
  }
  * { margin: 0; padding: 0; box-sizing: border-box; }
  html, body { width: 1200px; height: 1200px; overflow: hidden; }
  body { background: var(--stage); position: relative; font-family: "Open Sans", sans-serif; color: var(--ink); }

  .flyer-spread {
    position: absolute; left: 60px; top: 218px; width: 1080px; height: 764px;
    background: var(--paper); box-shadow: 0 14px 30px rgba(0,0,0,0.18);
    overflow: hidden;
  }

  /* Back page */
  .back-page { position: absolute; left: 0; top: 0; width: 530px; height: 764px;
    background: linear-gradient(160deg, var(--paper) 40%, var(--paper-soft) 70%, var(--paper) 100%); }
  .back-photo { position: absolute; left: 0; top: 0; width: 530px; height: 371px;
    background: linear-gradient(180deg, #8e8e8e 0%, #d8d8d8 45%, #bdbdbd 70%, #e9e9e9 100%); }
  .plan-line { position: absolute; background: var(--line); }
  .plan-line.v-left { left: 66px; top: 0; width: 1px; height: 392px; }
  .plan-line.v-right { left: 476px; top: 0; width: 1px; height: 505px; }
  .plan-line.h-bottom { left: 66px; top: 501px; width: 385px; height: 1px; }
  .quote-mark { position: absolute; font-family: Georgia, serif; font-size: 70px; color: #c9c9c9; line-height: 1; }
  .quote-mark.open { left: 38px; top: 405px; }
  .quote-mark.close { left: 445px; top: 470px; }
  .back-quote { position: absolute; left: 100px; top: 418px; width: 345px; text-align: center;
    font-style: italic; font-size: 14px; line-height: 20px; color: var(--ink-dark); }
  .brand-name { font-family: "Open Sans", sans-serif; font-weight: 600; color: var(--ink-dark); text-transform: uppercase; text-align: center; }
  .brand-mark { display: flex; flex-direction: column; align-items: center; gap: 6px; }
  .brand-square { background: var(--ink-dark); }
  .back-brand { position: absolute; left: 171px; top: 566px; width: 200px; }
  .back-brand .brand-square { width: 12px; height: 12px; }
  .back-brand .brand-name { font-size: 11px; letter-spacing: 1px; }
  .contact-list { position: absolute; left: 115px; top: 648px; width: 310px; list-style: none;
    text-align: center; font-size: 10px; line-height: 16.5px; color: var(--ink-dark); }
  .contact-list svg { width: 9px; height: 9px; vertical-align: -1px; margin-right: 4px; fill: var(--ink-dark); }

  .fold { position: absolute; left: 530px; top: 0; width: 9px; height: 764px;
    background: linear-gradient(90deg, #e4e4e4, #fafafa); }

  /* Front page */
  .front-column { position: absolute; left: 539px; top: 0; width: 254px; height: 764px; background: var(--paper-soft); }
  .front-brand { position: absolute; left: 545px; top: 62px; width: 242px; }
  .front-brand .brand-square { width: 18px; height: 18px; }
  .front-brand .brand-name { font-size: 15px; letter-spacing: 1.5px; line-height: 20px; }
  .headline { position: absolute; left: 567px; top: 208px; font-family: "Oswald", sans-serif; color: var(--ink); text-transform: uppercase; }
  .headline .lead { display: block; font-weight: 300; font-size: 24px; line-height: 28px; }
  .headline .main { display: block; font-weight: 600; font-size: 56px; line-height: 60px; letter-spacing: -1px; color: var(--ink-dark); }
  .headline .tail { display: block; font-weight: 300; font-size: 33px; line-height: 46px; color: var(--ink-dark); }
  .hero-photo { position: absolute; left: 793px; top: 0; width: 287px; height: 764px;
    background: linear-gradient(180deg, var(--sky) 0%, #bfe2f8 12%, #f4f4f4 22%, #e2e4e6 55%, #6f7d62 72%, #2f56c8 84%, #a9795a 92%, #8a6248 100%); }
  .listing-photo { position: absolute; border: 6px solid var(--paper); box-shadow: 0 3px 8px rgba(0,0,0,0.2); }
  .listing-photo.one { left: 559px; top: 525px; width: 147px; height: 120px;
    background: linear-gradient(180deg, #4c86d8 0%, #e8eef4 35%, #c9cfd6 65%, #5fa84a 82%, #3fb5e6 100%); }
  .listing-photo.two { left: 723px; top: 525px; width: 144px; height: 122px;
    background: linear-gradient(180deg, #2f62c4 0%, #e9ecef 40%, #b4b9bd 62%, #6f7a5c 85%, #8b8f8a 100%); }
  .listing-photo.three { left: 902px; top: 522px; width: 160px; height: 132px;
    background: linear-gradient(180deg, #1f63d6 0%, #e8e4d8 38%, #d9c9a6 55%, #3ec3e8 75%, #2a9fd4 100%); }
  .read-on-banner { position: absolute; left: 754px; top: 697px; width: 326px; height: 44px; background: var(--banner);
    display: flex; align-items: center; justify-content: center;
    font-family: "Oswald", sans-serif; font-weight: 300; font-size: 15px; color: #f0f0f0; text-transform: uppercase; }
</style>
</head>
<body>
  <main class="flyer-spread">
    <section class="back-page">
      <div class="back-photo" role="img" aria-label="Black and white photo of a modern white villa with infinity pool"></div>
      <span class="plan-line v-left"></span>
      <span class="plan-line v-right"></span>
      <span class="plan-line h-bottom"></span>
      <span class="quote-mark open">“</span>
      <span class="quote-mark close">”</span>
      <p class="back-quote">If you want service that matches the value of your home, contact us today for a private, personalised consultation. Brightline Villas Estepona. It’s all we do.</p>
      <div class="brand-mark back-brand">
        <span class="brand-square"></span>
        <span class="brand-name">Brightline Villas Estepona</span>
      </div>
      <ul class="contact-list">
        <li><svg viewBox="0 0 10 10"><path d="M5 0a3.4 3.4 0 0 0-3.4 3.4C1.6 6 5 10 5 10s3.4-4 3.4-6.6A3.4 3.4 0 0 0 5 0zm0 4.8a1.4 1.4 0 1 1 0-2.8 1.4 1.4 0 0 1 0 2.8z"/></svg>Suite 14 Torrenova Office Park</li>
        <li>Calle Los Almendros, Valdemoro, Marbella</li>
        <li><svg viewBox="0 0 10 10"><path d="M2 0.5l2 2.2-1 1.2c.6 1.3 1.6 2.3 2.9 2.9l1.2-1 2.2 2-1.2 1.7C4.8 9.3.7 5.2.3 1.7z"/></svg>+34 952 418 306</li>
        <li><svg viewBox="0 0 10 10"><circle cx="5" cy="5" r="5"/></svg>+34 677 342 815</li>
        <li><svg viewBox="0 0 10 10"><path d="M0 2h10v6H0zM0 2l5 3.5L10 2" /></svg>info@brightlinevillasestepona.example</li>
        <li><svg viewBox="0 0 10 10"><circle cx="5" cy="5" r="4.5"/></svg>www.brightlinevillasestepona.example</li>
      </ul>
    </section>

    <span class="fold"></span>

    <section class="front-page">
      <div class="front-column"></div>
      <div class="brand-mark front-brand">
        <span class="brand-square"></span>
        <span class="brand-name">Brightline Villas Estepona</span>
      </div>
      <h1 class="headline">
        <span class="lead">Helping you sell</span>
        <span class="main">Your<br>Modern<br>Home.</span>
        <span class="tail">It’s all we do!</span>
      </h1>
      <div class="hero-photo" role="img" aria-label="Modern white villa against blue sky with garden, pool and timber deck"></div>
      <div class="listing-photo one" role="img" aria-label="White terraced villa with lawn and pool"></div>
      <div class="listing-photo two" role="img" aria-label="Contemporary villa with terraces and garden"></div>
      <div class="listing-photo three" role="img" aria-label="Villa with large swimming pool"></div>
      <div class="read-on-banner">If you are thinking of selling, read on…</div>
    </section>
  </main>
</body>
</html>
```